Pennavora Web Design Project

We will need only one logo for Pennavora
Front Page
Header - Pennavora (logo) - Sites - Categories - Featured Contributors - Login (end header - the way plotharbor does this is great, but I'm open to new ideas also)
(Start Page Content)
Pennavora (logo - centered)
quirkyhourly.com - thezephant.com - stokingmoss.com (please leave spaces where we can place screenshots of those pages)
Sign Up!
Pennavora is a constantly growing network of sites that are dedicated to create relevant and well written content. If you are a student, professional, or a retiree, and you have an idea about a website that you would like to Contribute to, then this is the community that you have been looking for.
How It Works
Contribute An Article - Get Published - Increase Your Digital Footprint
Why We Exist
In the days when newspapers and radio stations dictated what the public read and heard, writers and editors were the gatekeepers in front of knowledge.
Those days are over and the lines between people who read content and publish content have become blurred. The outer-space like vastness of the internet is made larger exponentially every second by people who contribute data to it.
We believe that the future of knowledge in this world will have no gatekeepers and that every person is a contributor. This belief has lead to the creation of Pennavora.
Pennavora (logo-centered) - By The People, For The People
Footer
Follow Us: facebook, twitter, google+, youtube, instagram, linked in
____________________________
Categories Page (will need it's own page)
Arts & Entertainment - quirkyhourly.com
Health & Fitness - stokingmoss.com
News - thezephant.com
If you’re interested in contributing to a topic listed below please email us at info@pennavora.com
Automotive
Business
Careers
Education
Family & Parenting
Personal Finance
Food & Drink
Hobbies & Interests
Home & Garden
Law, Government & Politics
Society
Science
Pets
Sports
Style & Fashion
Technology & Computing
Travel
Real Estate
Shopping
Religion and Spirituality
Uncategorized
___________________________
Sites Page (will need it's own page)
Quirky Hourly - quirkyhourly.com is an Arts & Entertainment website consisting of photo galleries and descriptions.
The Zephant - thezephant.com is a News website that is specifically dedicated to newly trending topics.
Stoking Moss - stokingmoss.com is a Health & Fitness website where visitors can find articles about workout routines, health supplements, and get ideas for eating clean.
_________________________
Featured Contributors Page (will need it's own page)
Content is to be determined
__________________________
NOTES FOR DESIGNER
We also will need a two column sub page that with one column being thin for navigation. We really like the simplicity of tidleno.com and plotharbor.com. Those are two sites you can reference for the direcion we are heading in.
Thanks!
-Corey
Updates
Hey Everyone!

```html
<!DOCTYPE html>
<html lang="en">
<head>
<meta charset="utf-8">
<title>Pennavora — By the People, For the People</title>
<link rel="stylesheet" href="https://fonts.googleapis.com/css2?family=Open+Sans:wght@400;600&family=Advent+Pro:wght@300;400&family=Alegreya+SC&family=Alegreya:wght@400&family=Roboto+Slab:wght@800&display=swap">
<style>
  :root {
    --bar: #2b2b2b;
    --bar-side: #454545;
    --footer: #262626;
    --rule: #c9c9c9;
    --rule-dark: #4a4a4a;
    --ink: #222;
    --body: #333;
    --muted: #555;
    --accent: #4499ee;
    --link: #3a8ee0;
    --pale-green: #d9e8d3;
    --paper: #f3f3f0;
    --white: #fff;
  }
  * { box-sizing: border-box; margin: 0; padding: 0; }
  html, body { width: 1000px; height: 1200px; overflow: hidden; }
  body { position: relative; background: var(--white); font-family: "Open Sans", sans-serif; color: var(--body); }
  .abs { position: absolute; }
  .thin { font-family: "Advent Pro", sans-serif; font-weight: 300; }

  /* top bar */
  .topbar { left: 0; top: 0; width: 838px; height: 44px; background: var(--bar); border-bottom: 1px solid #111; }
  .topbar-side { left: 838px; top: 0; width: 162px; height: 44px; background: var(--bar-side); }
  .brand { left: 10px; top: 6px; display: flex; align-items: center; gap: 14px; }
  .brand-dot { width: 32px; height: 32px; border-radius: 50%; background: var(--accent); }
  .brand-name { font-family: "Roboto Slab", serif; font-weight: 800; font-size: 21px; color: var(--white); }
  .tagline { left: 595px; top: 16px; font-family: "Advent Pro", sans-serif; font-size: 15px; letter-spacing: 1px; color: #ddd; }
  .account { top: 16px; color: var(--white); font-size: 14px; }

  /* hero */
  .hero { left: 0; top: 44px; width: 802px; height: 352px;
    background: linear-gradient(100deg, #d8d2c6 0%, #b8a89a 22%, #8fb9a6 38%, #c9d6dc 55%, #a8c4d6 72%, #e4e7ea 100%); }
  .navband { left: 0; top: 44px; width: 802px; height: 100px; background: rgba(20,20,20,.78); }
  .nav { left: 75px; top: 58px; display: flex; gap: 20px; color: var(--white); font-size: 15px; }
  .subnav { left: 140px; top: 80px; font-family: "Advent Pro", sans-serif; font-size: 10.5px; line-height: 12.5px; color: #eee; letter-spacing: .5px; }
  .phone { left: 607px; top: 58px; color: var(--white); font-size: 14.5px; }
  .promo { left: 57px; width: 236px; background: rgba(90,140,210,.62); color: var(--white); text-align: center; }
  .promo-a { top: 144px; height: 110px; font-family: "Alegreya", serif; font-size: 19px; padding-top: 6px; text-align: left; padding-left: 17px; }
  .promo-a .big { font-family: "Alegreya SC", serif; font-size: 24px; display: block; margin-top: 8px; margin-left: 2px; }
  .promo-b { top: 257px; height: 50px; font-family: "Alegreya", serif; font-size: 16px; line-height: 21px; padding-top: 3px; }
  .foot-badge { left: 273px; top: 283px; }

  .rail { left: 49px; top: 44px; width: 1px; height: 1156px; background: var(--rule); }
  .rail-top { left: 49px; top: 44px; width: 1px; height: 98px; background: #777; }

  /* sections */
  .label { font-family: "Advent Pro", sans-serif; font-size: 15px; color: var(--muted); letter-spacing: .5px; }
  .hr { left: 49px; width: 753px; height: 1px; background: var(--rule); }
  .collage { left: 142px; top: 447px; width: 214px; height: 129px;
    background: linear-gradient(135deg, #8a5a6a, #c9b48c 40%, #6c8aa0 70%, #b3847a); }
  .qh-mark { left: 88px; top: 556px; width: 92px; height: 48px; background: var(--white);
    font-family: "Open Sans", sans-serif; font-weight: 600; font-size: 30px; color: #111; line-height: 48px; }
  .feature-title { left: 393px; top: 416px; font-size: 28px; color: var(--ink); letter-spacing: .5px; }
  .site-link { color: var(--link); font-size: 14.5px; }
  .desc { font-size: 12.5px; line-height: 16px; color: var(--body); }
  .readon { font-size: 13px; color: var(--ink); }
  .readon b { color: var(--link); font-weight: 400; }
  .kicker { font-family: "Advent Pro", sans-serif; font-size: 12px; color: var(--muted); }
  .blog-title { font-size: 21px; color: var(--ink); }

  /* carousel */
  .arrow-box { top: 832px; height: 126px; background: #eee; border: 1px solid #ddd; display: flex; align-items: center; justify-content: center; }
  .tile { top: 832px; width: 147px; height: 126px; }
  .tile-blue { background: var(--accent); }
  .tile-photo { background: linear-gradient(160deg, #e6e6e6, #a9a9a9 60%, #8a7a5e); }
  .tile-cap { position: absolute; left: 0; bottom: 0; width: 100%; height: 25px; background: #000; color: var(--white); font-size: 13px; padding: 4px 0 0 5px; }

  /* side column */
  .side-links { left: 803px; top: 44px; width: 197px; height: 34px; background: var(--white); font-size: 12px; color: #bbb; display: flex; gap: 7px; padding: 9px 0 0 44px; }
  .side-creative { left: 803px; top: 78px; width: 197px; height: 220px; background: var(--pale-green); }
  .side-creative span { position: absolute; left: 44px; top: 138px; font-family: "Advent Pro", sans-serif; font-weight: 300; font-size: 36px; color: var(--white); letter-spacing: 2px; }
  .side-tabs { left: 803px; top: 298px; width: 197px; height: 32px; background: var(--paper); font-family: "Advent Pro", sans-serif; font-size: 15px; color: var(--muted); display: flex; gap: 30px; padding: 6px 0 0 48px; letter-spacing: .5px; }
  .side-photo-a { left: 803px; top: 330px; width: 197px; height: 346px; background: linear-gradient(180deg, #f2ece6, #e7dcd2 50%, #ede6df); }
  .side-share { left: 803px; top: 676px; width: 197px; height: 99px; background: rgba(120,120,120,.75); }
  .side-share p { position: absolute; left: 21px; top: 0; color: var(--white); font-size: 31px; line-height: 31px; letter-spacing: -.5px; }
  .side-share b { font-weight: 600; font-size: 34px; }
  .side-photo-b { left: 803px; top: 775px; width: 197px; height: 269px; background: linear-gradient(160deg, #e8e8e8, #d9d2cc 50%, #e8c6a8); }
  .side-rail { left: 838px; top: 0; width: 1px; height: 1200px; background: rgba(255,255,255,.45); }

  /* footer */
  .footer { left: 0; top: 1044px; width: 1000px; height: 156px; background: var(--footer); }
  .fnav { left: 83px; top: 1053px; display: flex; gap: 0; font-family: "Advent Pro", sans-serif; font-size: 16px; color: #e6e6e6; letter-spacing: .5px; }
  .fnav span { width: 88px; }
  .fline-v { width: 1px; background: var(--rule-dark); }
  .copy { left: 80px; top: 1165px; font-family: "Advent Pro", sans-serif; font-size: 12px; color: #eee; }
  .fmail { left: 676px; top: 1166px; font-family: "Advent Pro", sans-serif; font-size: 14px; color: #eee; letter-spacing: .5px; }
  .social { display: flex; }
</style>
</head>
<body>

<!-- hero imagery -->
<div class="abs hero" role="img" aria-label="Photo of a woman reading a newspaper at a café table"></div>
<div class="abs navband"></div>

<!-- top bar -->
<header>
  <div class="abs topbar"></div>
  <div class="abs topbar-side"></div>
  <div class="abs brand"><span class="brand-dot"></span><span class="brand-name">Pennavora</span></div>
  <div class="abs tagline">BY THE PEOPLE, FOR THE PEOPLE</div>
  <div class="abs account" style="left:845px">Login</div>
  <div class="abs account" style="left:919px">Sign Up</div>

  <nav class="abs nav"><span>Home</span><span>Articles</span><span>Recent</span><span>Latest</span><span>Join</span></nav>
  <div class="abs subnav">Arts<br>Health<br>Fitness<br>Business</div>
  <div class="abs phone">Talk to Us: 555-0190-2476</div>

  <svg class="abs" style="left:600px;top:98px" width="190" height="28" viewBox="0 0 190 28" aria-label="Social links">
    <g fill="#bdbdbd">
      <circle cx="13" cy="14" r="12"/><circle cx="67" cy="14" r="12"/><circle cx="121" cy="14" r="12"/><circle cx="175" cy="14" r="12"/>
    </g>
    <g fill="none" stroke="#fff" stroke-width="1.6">
      <rect x="5" y="8" width="16" height="11" rx="1"/><path d="M5 9 L13 15 L21 9"/>
    </g>
  </svg>
</header>

<div class="abs rail-top"></div>

<!-- hero promo -->
<div class="abs promo promo-a">Contribute An Article<span class="big">Get Published</span></div>
<div class="abs promo promo-b">incease your digital<br>FOOTPRINT</div>
<svg class="abs foot-badge" width="54" height="54" viewBox="0 0 54 54" aria-hidden="true">
  <circle cx="27" cy="27" r="27" fill="var(--accent)"/>
  <g fill="#fff">
    <ellipse cx="28" cy="30" rx="5" ry="9"/>
    <circle cx="24" cy="18" r="1.8"/><circle cx="27.5" cy="16.5" r="1.6"/><circle cx="30.5" cy="17" r="1.4"/><circle cx="33" cy="18.5" r="1.2"/>
  </g>
</svg>

<div class="abs rail"></div>

<!-- just launched -->
<section>
  <div class="abs label" style="left:70px;top:405px">JUST LAUNCHED
    <svg width="14" height="10" viewBox="0 0 14 10" style="margin-left:3px"><path d="M1 2 L7 8 L13 2" fill="none" stroke="var(--accent)" stroke-width="2.5"/></svg>
  </div>
  <div class="abs collage" role="img" aria-label="Collage of arts and entertainment photos"></div>
  <div class="abs qh-mark">Q&amp;H</div>
  <h2 class="abs feature-title" style="font-weight:400">ARTS &amp; ENTERTAINMENT</h2>
  <div class="abs site-link" style="left:391px;top:487px">quirkyhourly.com</div>
  <p class="abs desc" style="left:391px;top:515px;width:340px">quirkyhourly.com is an Arts &amp; Entertainment website consisting of photo galleries and descriptions</p>
  <div class="abs readon" style="left:391px;top:563px">READ ON<b>&gt;</b></div>
</section>

<div class="abs hr" style="top:616px"></div>

<!-- on our minds -->
<section>
  <div class="abs label" style="left:68px;top:625px">ON OUR MINDS</div>
  <div class="abs kicker" style="left:93px;top:648px">BLOG</div>
  <h3 class="abs blog-title" style="left:93px;top:661px;font-weight:400">WHY WE EXIST!</h3>
  <p class="abs desc" style="left:92px;top:693px;width:310px">In the days when newspapers and radio stations dictat-ed what the public read and heard, writers and editors .were the gatekeepers in front of knowledge<br>Those days are over and the lines between people who read content and publish</p>
  <div class="abs readon" style="left:335px;top:771px">READ ON<b>&gt;</b></div>

  <div class="abs kicker" style="left:435px;top:648px">BLOG</div>
  <h3 class="abs blog-title" style="left:434px;top:661px;font-weight:400">HOW IT WORKS</h3>
  <p class="abs desc" style="left:434px;top:693px;width:320px">If you are a student, professional, or a retiree, and you have an idea about a website that you would like to Contribute to, then this is the community that you have been looking for</p>
  <div class="abs readon" style="left:683px;top:771px">READ ON<b>&gt;</b></div>
</section>

<div class="abs hr" style="top:785px"></div>

<!-- sites carousel -->
<section>
  <div class="abs hr" style="top:832px"></div>
  <div class="abs hr" style="top:957px"></div>
  <div class="abs arrow-box" style="left:50px;width:37px">
    <svg width="16" height="50" viewBox="0 0 16 50"><path d="M13 2 L3 25 L13 48" fill="none" stroke="#c4c4c4" stroke-width="4"/></svg>
  </div>
  <div class="abs tile tile-photo" style="left:97px" role="img" aria-label="Screenshot of stokingmoss.com: dumbbells and an apple">
    <div class="tile-cap">stokingmoss.com</div>
  </div>
  <div class="abs tile tile-blue" style="left:268px"></div>
  <div class="abs tile tile-photo" style="left:435px;background:linear-gradient(170deg,#f0f0f0,#dcdcdc 50%,#8a6a4c)" role="img" aria-label="Screenshot of thezephant.com: small kitten in a boot">
    <div class="tile-cap">thezephant.com</div>
  </div>
  <div class="abs tile tile-blue" style="left:604px"></div>
  <div class="abs arrow-box" style="left:762px;width:40px">
    <svg width="16" height="50" viewBox="0 0 16 50"><path d="M3 2 L13 25 L3 48" fill="none" stroke="#c4c4c4" stroke-width="4"/></svg>
  </div>
</section>

<!-- side column -->
<aside>
  <div class="abs side-links"><span>Home</span><span>|</span><span>Article</span><span>|</span><span>Recent</span></div>
  <div class="abs side-creative"><span>Creative</span></div>
  <div class="abs side-tabs"><span>STORY</span><span>PUBLISH</span></div>
  <div class="abs side-photo-a" role="img" aria-label="Faded fashion photo of a model in a white dress"></div>
  <div class="abs side-share"><p>SHARE<br><b>YOUR</b><br><b>STORY</b></p></div>
  <div class="abs side-photo-b" role="img" aria-label="Faded photo of a tablet showing a website beside oranges"></div>
  <div class="abs side-rail"></div>
</aside>

<!-- footer -->
<footer>
  <div class="abs footer"></div>
  <div class="abs fline-v" style="left:49px;top:1044px;height:156px"></div>
  <div class="abs fline-v" style="left:587px;top:1044px;height:156px"></div>
  <div class="abs fline-v" style="left:838px;top:1044px;height:156px"></div>
  <div class="abs" style="left:49px;top:1155px;width:789px;height:1px;background:var(--rule-dark)"></div>
  <nav class="abs fnav"><span>Home</span><span>Articles</span><span>Recent</span><span>Latest</span><span>Join</span></nav>
  <div class="abs fnav" style="left:604px">Contact</div>
  <div class="abs copy">© 2013 .Pennavora.Inc All Rights Reserved</div>
  <svg class="abs" style="left:393px;top:1162px" width="190" height="26" viewBox="0 0 190 26" aria-label="Social links">
    <g fill="#bdbdbd">
      <circle cx="13" cy="13" r="12"/><circle cx="67" cy="13" r="12"/><circle cx="121" cy="13" r="12"/><circle cx="175" cy="13" r="12"/>
    </g>
    <g fill="none" stroke="#fff" stroke-width="1.6">
      <rect x="5" y="7" width="16" height="11" rx="1"/><path d="M5 8 L13 14 L21 8"/>
    </g>
  </svg>
  <div class="abs fmail">info@pennavora.com</div>
</footer>

</body>
</html>
```